Brochure for a civil enineering company in A4 format

I need a brochure design for our company VELTA Engineering S.r.l.. We are an engineering consultant company. Our main clients are from the infrastructure industry (geotechnical and underground sectors mainly).
We are looking for a 2 pages (4 faces) fold out design with a glued pocket where we can put individual data sheets.
I need A4 format pages.

Target Market(s)

We are an engineering consultant company. Our main clients are from the infrastructure industry (geotechnical and underground sectors mainly).

Industry/Entity Type

Civil Engineer

Font styles to use
Sans Serif

Requirements
Must have
• Overall: 2 pages in A4 format
Essential style. Bright and modern appearance.
Glued pocket
Logo integrated in a picture on the pocket where I would like to insert a slogan (… velta engineering … reliable solutions …)
Attached are selected images which the designer can use and edit at their own discretion.
Some advice in the following (anyway designers are free to provide their solutions):
Outer sheets:
Front page with name, logo. It could be nice to have the “m” of the logo integrated in a pictures, also a modified picture (I mean modify one of the attached pictures) so to create a general image and do not tie the cover to a specific job.
Back page: offices address and contact email address. Nice to have one space for a slogan.
Inner sheet: text that I upload in the file “inside-sheets”, possibly with pictures on each sheet. In the right faces insert the glued pocket. On this pages insert the section OUR EXPERIENCE ….with a space for a picture of our team.
Nice to have
• Clean and essential design.
Pictures choosing from the atteched ones. Pictures could be modified in a very light manner to make them a general idea of the work ( I mean geotechnical world) without to be immediately linked to a specific site.
Should not have
• excessive frills

```html
<!DOCTYPE html>
<html lang="it">
<head>
<meta charset="utf-8">
<title>VELTA Engineering – Brochure</title>
<link href="https://fonts.googleapis.com/css2?family=Ubuntu:wght@400;500;700&family=Source+Sans+3:wght@400;600&family=Oswald:wght@400;500&display=swap" rel="stylesheet">
<style>
:root{
  --bg:#d6d6d6;
  --paper:#ffffff;
  --ink:#1d1d22;
  --text:#3a3a40;
  --red:#c4202b;
  --dark:#24262f;
  --dark2:#3a3c47;
  --grey:#8a8a8e;
  --light:#c8c8ca;
}
*{box-sizing:border-box;margin:0;padding:0}
html,body{width:1164px;height:1200px;overflow:hidden;background:var(--bg)}
body{font-family:"Source Sans 3",sans-serif;color:var(--text)}
.canvas{position:relative;width:1164px;height:1200px}
.abs{position:absolute}
.sheet{position:absolute;left:66px;width:1032px;height:486px;background:var(--paper)}
.sheet--outer{top:54px}
.sheet--inner{top:612px}
.panel-left{position:absolute;left:0;top:0;width:344px;height:486px;overflow:hidden}
.photo{position:absolute}
.hex{position:absolute;clip-path:polygon(50% 0,100% 25%,100% 75%,50% 100%,0 75%,0 25%);background:#fff}
.hex > .hex-fill{position:absolute;inset:3px;clip-path:polygon(50% 0,100% 25%,100% 75%,50% 100%,0 75%,0 25%)}
.heading{font-family:"Ubuntu",sans-serif;font-weight:500;color:var(--ink);letter-spacing:.3px}
.body-copy{font-size:7px;line-height:10.3px;text-align:justify}
.body-copy p+p{margin-top:10px}
.slogan{font-family:"Ubuntu",sans-serif;color:var(--red)}
.brand{font-family:"Ubuntu",sans-serif;font-weight:700;letter-spacing:1px}
/* founders */
.founders-tab{left:14px;top:229px;width:146px;height:15px;background:var(--red);clip-path:polygon(0 0,88% 0,100% 100%,0 100%);color:#fff;font-size:6.2px;line-height:15px;padding-left:5px}
.founder{position:absolute;left:14px;width:316px;height:50px}
.founder .hex{left:0;top:0;width:36px;height:41px;background:#ececec}
.founder .hex-fill{background:linear-gradient(#9a9a9a,#5a5a5a)}
.founder-name{position:absolute;left:44px;top:0;font-size:4.8px;color:var(--red);text-transform:uppercase}
.founder-bio{position:absolute;left:44px;top:6px;width:272px;font-size:4.4px;line-height:5.6px;text-align:justify;color:#333}
/* contacts */
.office{position:absolute;top:424px;font-size:7.6px;line-height:10.4px;color:#555}
.office h3{font-family:"Ubuntu",sans-serif;font-weight:500;color:var(--red);font-size:9.4px;margin-bottom:2px}
.office .row{display:flex;align-items:center;gap:4px}
.office svg{width:6px;height:6px;flex:none}
.office .indent{padding-left:10px}
/* services list */
.service{position:absolute;width:316px;display:flex;gap:9px;font-size:6.6px;line-height:9px}
.service .icon{flex:none;width:27px;height:27px;clip-path:polygon(50% 0,100% 25%,100% 75%,50% 100%,0 75%,0 25%);background:var(--red);display:flex;align-items:center;justify-content:center}
.service .icon svg{width:14px;height:14px}
</style>
</head>
<body>
<div class="canvas">

  <!-- OUTER SHEET -->
  <section class="sheet sheet--outer" aria-label="Lato esterno">
    <div class="panel-left">
      <div class="photo" style="left:0;top:0;width:344px;height:129px;background:linear-gradient(180deg,#b9c4c9 0%,#8c8a7d 45%,#6e6756 100%)" role="img" aria-label="Cantiere con imbocchi di due gallerie e gru su un versante collinare"></div>
      <div class="hex" style="left:251px;top:84px;width:83px;height:93px"><div class="hex-fill" style="background:radial-gradient(circle at 50% 55%,#8a7f73,#3b3631)" role="img" aria-label="Interno di galleria con macchina di perforazione rossa"></div></div>
      <h2 class="heading abs" style="left:15px;top:139px;font-size:20px">OUR COMPANY</h2>
      <p class="body-copy abs" style="left:14px;top:172px;width:319px">La società nasce dall’associazione di un gruppo di professionisti, con indiscusse competenze ed affidabilità, con esperienza maturata in oltre trent’anni di attività come progettisti e consulenti nel settore delle grandi opere di ingegneria civile; geologia, ingegneria geotecnica ed idraulica ed opere sotterranee sono il “core” delle loro competenze ….</p>
      <div class="founders-tab abs">I SOCI FONDATORI SONO:</div>

      <div class="founder" style="top:252px">
        <div class="hex"><div class="hex-fill" role="img" aria-label="Ritratto del socio fondatore"></div></div>
        <div class="founder-name">Marco</div>
        <p class="founder-bio">Già Direttore Tecnico e Socio di NORDA Srl fino al 2018, ha firmato gran parte dei progetti nel campo delle opere sotterranee e dell’ingegneria geotecnica. Dal 2019 è Direttore Tecnico di TERVA. Vanta oltre 150 gallerie naturali e numerosi progetti di assistenza tecnica nel campo delle strutture geotecniche e delle sistemazioni idrogeologiche. Negli ultimi dieci anni è stato responsabile di attività di assistenza tecnica per imprese di costruzione, su opere di valore superiore a 440 Mio EUR, e di verifica e validazione in Italia e all’estero per oltre 3.400 Mio EUR.</p>
      </div>
      <div class="founder" style="top:307px">
        <div class="hex"><div class="hex-fill" role="img" aria-label="Ritratto del socio fondatore"></div></div>
        <div class="founder-name">Luca</div>
        <p class="founder-bio">Luca, 30 anni di esperienza professionale. Coinvolto in oltre 150 gallerie naturali per più di 360 km complessivi. Numerosi progetti e attività di assistenza tecnica nel campo delle strutture, delle sistemazioni idrogeologiche e delle opere di protezione ambientale. Responsabile di assistenza tecnica in corso d’opera per imprese di costruzione su opere oltre 440 Mio EUR, con attività di verifica ai fini della validazione in Italia e all’estero per oltre 3.400 Mio EUR.</p>
      </div>
      <div class="founder" style="top:360px">
        <div class="hex"><div class="hex-fill" role="img" aria-label="Ritratto della socia fondatrice"></div></div>
        <div class="founder-name">Giulia</div>
        <p class="founder-bio">Giulia, 30 anni di esperienza professionale. Coinvolta in oltre 150 gallerie naturali per più di 360 km complessivi. Numerosi progetti e attività di assistenza tecnica nel campo delle strutture, delle sistemazioni idrogeologiche e delle opere di protezione ambientale. Responsabile di assistenza tecnica in corso d’opera per imprese di costruzione su opere oltre 440 Mio EUR, con attività di verifica ai fini della validazione in Italia e all’estero per oltre 3.400 Mio EUR.</p>
      </div>
      <div class="founder" style="top:415px">
        <div class="hex"><div class="hex-fill" role="img" aria-label="Ritratto della socia fondatrice"></div></div>
        <div class="founder-name">Sara</div>
        <p class="founder-bio">Sara, 30 anni di esperienza professionale. Coinvolta in oltre 150 gallerie naturali per più di 360 km complessivi. Numerosi progetti e attività di assistenza tecnica nel campo delle strutture, delle sistemazioni idrogeologiche e delle opere di protezione ambientale. Responsabile di assistenza tecnica in corso d’opera per imprese di costruzione su opere oltre 440 Mio EUR, con attività di verifica ai fini della validazione in Italia e all’estero per oltre 3.400 Mio EUR.</p>
      </div>
      <div class="abs" style="left:0;top:474px;width:344px;height:12px;background:linear-gradient(90deg,var(--dark),var(--dark2))"></div>
    </div>

    <!-- dark band across back + front -->
    <div class="abs" style="left:345px;top:76px;width:687px;height:326px;background:linear-gradient(90deg,#1f2029,#2e303a 60%,#23252d)"></div>
    <div class="photo" style="left:577px;top:90px;width:455px;height:300px;background:radial-gradient(ellipse at 70% 40%,#d8d8d8 0%,#6d6d6d 22%,#2b2b2b 55%,#3a1517 85%,#1f1f22 100%)" role="img" aria-label="Interno di galleria illuminata con operai e riflessi sul fondo bagnato"></div>
    <div class="brand abs" style="left:380px;top:228px;font-size:40px;color:var(--light)">VELTA</div>
    <p class="slogan abs" style="left:402px;top:291px;font-size:13.5px;line-height:17px">velta engineering …<br>reliable solutions …</p>

    <!-- contacts -->
    <div class="office" style="left:362px">
      <h3>MILANO</h3>
      <div class="row"><svg viewBox="0 0 10 10"><path d="M5 0a3.4 3.4 0 0 0-3.4 3.4C1.6 6 5 10 5 10s3.4-4 3.4-6.6A3.4 3.4 0 0 0 5 0zm0 4.8a1.4 1.4 0 1 1 0-2.8 1.4 1.4 0 0 1 0 2.8z" fill="#c4202b"/></svg>Via Verdi, 14</div>
      <div class="indent">20121 Milano - IT</div>
      <div class="row"><svg viewBox="0 0 10 10"><path d="M2 0l2 2.4-1.2 1.4a6 6 0 0 0 3.4 3.4L7.6 6 10 8l-1.4 2C4 10 0 6 0 1.4z" fill="#c4202b"/></svg>+39 02 000011111</div>
      <div class="row"><svg viewBox="0 0 10 10"><rect y="2" width="10" height="6.5" fill="#c4202b"/><path d="M0 2l5 3.4L10 2" fill="none" stroke="#fff" stroke-width=".8"/></svg>info@veltaengineering.example</div>
    </div>
    <div class="abs" style="left:517px;top:419px;width:1px;height:55px;background:#d0d0d0"></div>
    <div class="office" style="left:529px">
      <h3>ARCO TN</h3>
      <div class="row"><svg viewBox="0 0 10 10"><path d="M5 0a3.4 3.4 0 0 0-3.4 3.4C1.6 6 5 10 5 10s3.4-4 3.4-6.6A3.4 3.4 0 0 0 5 0zm0 4.8a1.4 1.4 0 1 1 0-2.8 1.4 1.4 0 0 1 0 2.8z" fill="#c4202b"/></svg>Via dei Tigli, 9</div>
      <div class="indent">38062 Arco TN - IT</div>
      <div class="row"><svg viewBox="0 0 10 10"><path d="M2 0l2 2.4-1.2 1.4a6 6 0 0 0 3.4 3.4L7.6 6 10 8l-1.4 2C4 10 0 6 0 1.4z" fill="#c4202b"/></svg>+39 02 000011111</div>
      <div class="row"><svg viewBox="0 0 10 10"><rect y="2" width="10" height="6.5" fill="#c4202b"/><path d="M0 2l5 3.4L10 2" fill="none" stroke="#fff" stroke-width=".8"/></svg>info@veltaengineering.example</div>
    </div>

    <!-- cover -->
    <div class="brand abs" style="left:706px;top:26px;font-size:30px;color:var(--ink)">VELTA</div>
    <div class="abs" style="left:812px;top:38px;width:9px;height:9px;background:var(--red)"></div>
    <div class="abs" style="left:707px;top:62px;font-size:5px;letter-spacing:1.6px;color:#333;font-family:'Ubuntu',sans-serif">VELTA ENGINEERING , RELIABLE SOLUTIONS</div>
    <p class="slogan abs" style="left:934px;top:43px;font-size:10px;line-height:11.5px">velta engineering …<br>reliable solutions …</p>

    <div class="hex" style="left:882px;top:292px;width:75px;height:84px"><div class="hex-fill" style="background:linear-gradient(#d8d8d8,#6c6c6c)" role="img" aria-label="Escavatore all'interno di una galleria"></div></div>
    <div class="hex" style="left:843px;top:362px;width:75px;height:85px"><div class="hex-fill" style="background:radial-gradient(circle at 45% 55%,#e26a6e,#a51b24)" role="img" aria-label="Tubazione e gru di cantiere in tinta rossa"></div></div>
    <div class="hex" style="left:922px;top:353px;width:106px;height:119px"><div class="hex-fill" style="background:linear-gradient(160deg,#2c2e38,#14151b)"></div></div>
    <p class="abs" style="left:925px;top:398px;width:100px;text-align:center;font-family:'Oswald',sans-serif;font-size:7.4px;line-height:12px;color:#fff;white-space:nowrap">SCIENZE GEOLOGICHE,<br>DELL’INGEGNERIA GEOTECNICA<br>E DELL’INGEGNERIA IDRAULICA</p>
    <div class="abs" style="left:690px;top:463px;width:144px;height:14px;background:var(--red);clip-path:polygon(0 0,92% 0,100% 100%,0 100%);color:#fff;font-family:'Ubuntu',sans-serif;font-size:7.4px;line-height:14px;padding-left:17px">www.veltaengineering.example</div>
    <svg class="abs" style="left:696px;top:467px" width="7" height="7" viewBox="0 0 10 10" aria-hidden="true"><circle cx="5" cy="5" r="4.3" fill="none" stroke="#fff"/><path d="M.7 5h8.6M5 .7c-2.4 2.4-2.4 6.2 0 8.6M5 .7c2.4 2.4 2.4 6.2 0 8.6" fill="none" stroke="#fff" stroke-width=".8"/></svg>
  </section>

  <!-- INNER SHEET -->
  <section class="sheet sheet--inner" aria-label="Lato interno">
    <!-- pocket flap panel -->
    <div class="photo" style="left:0;top:0;width:344px;height:486px;background:linear-gradient(160deg,#f2f2f2 0%,#d9d9d9 50%,#bdbdbd 100%)" role="img" aria-label="Vista dall'alto in bianco e nero di uno scavo con armature e strutture in cemento"></div>
    <div class="abs" style="left:0;top:343px;width:344px;height:143px;background:linear-gradient(135deg,#2a2c36,#1e1f27);clip-path:polygon(0 0,95% 0,100% 100%,0 100%)"></div>
    <div class="brand abs" style="left:0;top:374px;width:335px;text-align:center;font-size:30px;color:#d6d6d8">VELTA</div>
    <div class="abs" style="left:0;top:410px;width:335px;text-align:center;font-size:4.6px;letter-spacing:1.5px;color:#c9c9cc;font-family:'Ubuntu',sans-serif">VELTA ENGINEERING , RELIABLE SOLUTIONS</div>
    <p class="abs" style="left:0;top:436px;width:335px;text-align:center;font-family:'Ubuntu',sans-serif;font-size:10px;color:#e6e6e8">velta engineering … reliable solutions …</p>

    <!-- top dark band -->
    <div class="abs" style="left:345px;top:0;width:687px;height:130px;background:linear-gradient(90deg,#2a2c36,#1e1f27)"></div>
    <div class="photo" style="left:346px;top:9px;width:348px;height:120px;background:linear-gradient(180deg,#6f6459 0%,#8a7e70 40%,#d57a3a 70%,#4a4a40 100%)" role="img" aria-label="Escavatore arancione e mezzo di perforazione verde all'imbocco di una galleria"></div>
    <h2 class="heading abs" style="left:728px;top:19px;font-size:19.5px;color:#fff">OUR SERVICES</h2>
    <div class="body-copy abs" style="left:728px;top:46px;width:292px;color:#d8d8dc">
      <p>Progettazione e consulenza specialistica nel campo della geologia, dell’ingegneria geotecnica, delle opere sotterranee e dell’ingegneria idtraulica.</p>
      <p>Aiutiamo i nostri clienti a risolvere problemi di natura progettuale, contrattuale e costruttiva che possono nascere nell’intera vita del progetto portando la nostra esperienza all’interno delle loro organizzazioni, migliorando la qualità dei loro servizi di ingegneria, ottimizzando i loro progetti, proponendo nuove idee e soluzioni, rafforzando i loro approcci ……</p>
    </div>

    <!-- our company -->
    <h2 class="heading abs" style="left:360px;top:148px;font-size:20px">OUR COMPANY</h2>
    <div class="body-copy abs" style="left:359px;top:186px;width:318px">
      <p>VELTA Engineering S.r.l. offre servizi di consulenza tecnica, contrattuale e strategica ai principali attori nei settori delle scienze geologiche, dell’ingegneria geotecnica e dell’ingegneria idraulica. Lavoriamo per mitigare il rischio e ridurre l’incertezza, con flessibilità nella ricerca della soluzione ottimale contribuendo ad aumentare la redditività del progetto.</p>
      <p>VELTA Engineering S.r.l. è una società indipendente che nasce nel luglio 2020 dall’associazione di un gruppo di professionisti che hanno messo a fattor comune la reciproca esperienza maturata in oltre trent’anni di attività come progettisti e consulenti nel settore delle grandi opere di ingegneria civile lavorando come Direttori Tecnici di Main Engineering Companies and as Freelancers.</p>
      <p>VELTA Engineering S.r.l. vuole unire l’esperienza dei Fondatori e delle figure chiave con l’entusiasmo di chi intraprende una nuova attività, per dare vita ad una nuova realtà che si pone come obbiettivo principale il design of infrastructures that are safe, sustainable and economic.<br>Each of our projects represents a long term commitment, we believe in providing safe, reliable, sustainable end innovative solutions. This is and will be our distinctive characteristic.</p>
    </div>

    <div class="abs" style="left:345px;top:417px;width:687px;height:69px;background:linear-gradient(90deg,#2a2c36,#1e1f27)"></div>
    <div class="hex" style="left:381px;top:366px;width:80px;height:96px"><div class="hex-fill" style="background:linear-gradient(#b9a48a,#7b7f86)" role="img" aria-label="Cantiere di fondazioni con armature"></div></div>
    <div class="hex" style="left:469px;top:361px;width:96px;height:108px"><div class="hex-fill" style="background:radial-gradient(circle at 50% 60%,#2d2824,#9c8a76)" role="img" aria-label="Imbocco di galleria in roccia"></div></div>
    <div class="hex" style="left:575px;top:366px;width:82px;height:96px"><div class="hex-fill" style="background:linear-gradient(#8fb6dc 0%,#cfe0ee 40%,#6f7d58 70%,#8b5a3a 100%)" role="img" aria-label="Viadotto in una valle collinare"></div></div>

    <!-- services detail -->
    <div class="body-copy abs" style="left:702px;top:186px;width:318px">
      <p>VELTA Engineering è in grado di fornire la propria assistenza nell’intero iter procedurale, dalla fase di indagine preliminare e di analisi di fattibilità fino alla progettazione costruttiva e all’assistenza tecnica in fase realizzativa.</p>
      <p>La specializzazione e l’esperienza accumulate nelle discipline della geologia, dell’ingegneria geotecnica e del sottosuolo e dell’idraulica ci permette di massimizzare la nostra efficacia quando sia necessario:</p>
    </div>
    <div class="service" style="left:702px;top:259px">
      <div class="icon"><svg viewBox="0 0 14 14"><circle cx="7" cy="7" r="3.4" fill="none" stroke="#fff" stroke-width="1.6"/><path d="M7 1v2M7 11v2M1 7h2M11 7h2M2.8 2.8l1.4 1.4M9.8 9.8l1.4 1.4M2.8 11.2l1.4-1.4M9.8 4.2l1.4-1.4" stroke="#fff" stroke-width="1.4"/></svg></div>
      <p style="text-align:justify">Far fronte a situazioni di emergenza anche su progetti in fase di sviluppo avanzato garantendo l’immediata focalizzazione delle problematiche di progetto e garantendo il risultato finale atteso (in termini di qualità, tempistiche e costi…)</p>
    </div>
    <div class="service" style="left:702px;top:297px">
      <div class="icon"><svg viewBox="0 0 14 14"><rect x="2.5" y="1.5" width="8" height="11" fill="none" stroke="#fff" stroke-width="1.2"/><path d="M4.5 4.5h4M4.5 7h4M4.5 9.5h2.5" stroke="#fff" stroke-width="1"/></svg></div>
      <p>Fornire “second opinion” di elevato valore tecnico ed amministrativo in occasione di problematiche progettuali e costruttive e dispute legali</p>
    </div>
    <div class="service" style="left:702px;top:333px">
      <div class="icon"><svg viewBox="0 0 14 14"><rect x="3" y="2" width="8" height="11" fill="none" stroke="#fff" stroke-width="1.2"/><rect x="5" y="1" width="4" height="2" fill="#fff"/><path d="M4.8 6l.8.8 1.2-1.4M4.8 9l.8.8 1.2-1.4M8 6h1.5M8 9h1.5" stroke="#fff" stroke-width=".9" fill="none"/></svg></div>
      <p>Analizzare in tempi brevi progetti svolti da terzi individuandone le “criticità”, verificandone la cantierabilità e la validità tecnico economica.</p>
    </div>
    <div class="service" style="left:702px;top:370px;width:220px">
      <div class="icon"><svg viewBox="0 0 14 14"><path d="M2 12.5h10" stroke="#fff" stroke-width="1"/><rect x="3" y="8.5" width="1.6" height="3.5" fill="#fff"/><rect x="5.8" y="6.5" width="1.6" height="5.5" fill="#fff"/><rect x="8.6" y="4.5" width="1.6" height="7.5" fill="#fff"/><path d="M2.5 7l4-3.5 2 1.5 3-3" stroke="#fff" stroke-width="1" fill="none"/></svg></div>
      <p>Ottimizzare i progetti redatti da terzi implementandone il contenuto e massimizzando l’efficacia economica degli investimenti.</p>
    </div>
    <div class="brand abs" style="left:736px;top:428px;font-size:26px;color:#4a4c56">VELTA</div>
    <a class="abs" style="left:737px;top:465px;font-family:'Ubuntu',sans-serif;font-size:8.6px;color:#e4e4e8;text-decoration:none">www.veltaengineering.example</a>
    <div class="photo" style="left:882px;top:398px;width:150px;height:88px;background:linear-gradient(170deg,#9aa08a 0%,#7d7a6e 50%,#a99c8a 100%);clip-path:polygon(0 18%,100% 0,100% 100%,0 100%);border-left:2px solid #fff" role="img" aria-label="Vista aerea di un'area di cantiere con capannoni e mezzi"></div>
  </section>

</div>
</body>
</html>
```